Criação de Folder para Automotivo
A empresa queria:
" A Vortan temos o seu histórico e outros elementos mais. A destacar que a Vortan se caracteriza pela qualidade dos seus produtos, possuindo cerca de 350 produtos certificados pelo BRANQUAL. "

```html
<!DOCTYPE html>
<html lang="pt-BR">
<head>
<meta charset="UTF-8">
<title>Vortan – Índice</title>
<link href="https://fonts.googleapis.com/css2?family=Montserrat:wght@400;500;700;800&display=swap" rel="stylesheet">
<style>
  :root{
    --red-deep:#7e0a12;
    --red:#c4141f;
    --red-bright:#e0232d;
    --ink:#2b2b2b;
    --rule:#3a3a3a;
    --dots:#6a6a6a;
    --paper-1:#f4f4f4;
    --paper-2:#dedede;
    --stage:#eeeeee;
    --white:#ffffff;
  }
  *{box-sizing:border-box;margin:0;padding:0}
  html,body{width:1200px;height:1200px;overflow:hidden}
  body{background:var(--stage);font-family:'Montserrat',sans-serif;color:var(--ink);position:relative}

  .index-page{position:absolute;left:20px;top:270px;width:1160px;height:660px;
    background:linear-gradient(180deg,var(--paper-1),var(--paper-2));overflow:hidden}

  .page-header{height:86px;display:flex;align-items:center;justify-content:space-between;padding:0 48px 0 76px;
    background:linear-gradient(90deg,var(--red-deep) 0%,var(--red) 30%,var(--red-bright) 55%,var(--red) 80%,var(--red-deep) 100%)}
  .page-title{color:var(--white);font-weight:800;font-size:38px;letter-spacing:1px}
  .brand{display:flex;align-items:center;gap:12px;color:var(--white);font-weight:700;font-size:34px;letter-spacing:4px;text-transform:uppercase}
  .brand-square{width:26px;height:26px;border:3px solid var(--white)}

  .watermark{position:absolute;left:30px;top:120px;width:260px;height:520px;
    background:radial-gradient(ellipse at 50% 45%,rgba(255,255,255,.7),rgba(255,255,255,0) 70%)}

  .index-section{position:absolute;left:0;width:1160px}
  .section-1{top:119px}.section-2{top:302px}.section-3{top:478px}

  .tab-row{position:relative;height:32px}
  .tab{position:absolute;top:0;height:32px;background:var(--red);color:var(--white);font-weight:700;font-size:18px;
    display:flex;align-items:center;padding-left:16px}
  .tab-rule{position:absolute;bottom:0;height:3px;background:var(--rule)}
  .tab-maker{left:0;width:300px;padding-left:76px}
  .rule-maker{left:300px;width:200px}
  .tab-displacement{left:518px;width:160px}
  .rule-displacement{left:678px;width:350px}
  .tab-page{left:1040px;width:108px;justify-content:center;padding-left:0}

  .entries{list-style:none;margin-top:16px}
  .entry{position:relative;height:24px;font-size:14px;font-weight:500}
  .entry span{position:absolute;top:3px}
  .part-name{left:76px}
  .part-leader{left:190px;width:315px;top:15px!important;border-bottom:2px dotted var(--dots)}
  .displacement{left:530px}
  .displacement-leader{left:630px;width:400px;top:15px!important;border-bottom:2px dotted var(--dots)}
  .page-number{left:1083px;font-size:12px}
</style>
</head>
<body>
<main class="index-page">
  <header class="page-header">
    <h1 class="page-title">ÍNDICE</h1>
    <div class="brand"><span class="brand-square"></span>Vortan</div>
  </header>

  <div class="watermark" role="img" aria-label="Ilustração de pistão em marca-d'água"></div>

  <section class="index-section section-1">
    <div class="tab-row">
      <div class="tab tab-maker">Nome Montadora</div><div class="tab-rule rule-maker"></div>
      <div class="tab tab-displacement">Cilindarada</div><div class="tab-rule rule-displacement"></div>
      <div class="tab tab-page">Página</div>
    </div>
    <ul class="entries">
      <li class="entry"><span class="part-name">Nome Peça</span><span class="part-leader"></span><span class="displacement">Cilindrada</span><span class="displacement-leader"></span><span class="page-number">001</span></li>
      <li class="entry"><span class="part-name">Nome Peça</span><span class="part-leader"></span><span class="displacement">Cilindrada</span><span class="displacement-leader"></span><span class="page-number">002</span></li>
      <li class="entry"><span class="part-name">Nome Peça</span><span class="part-leader"></span><span class="displacement">Cilindrada</span><span class="displacement-leader"></span><span class="page-number">003</span></li>
      <li class="entry"><span class="part-name">Nome Peça</span><span class="part-leader"></span><span class="displacement">Cilindrada</span><span class="displacement-leader"></span><span class="page-number">004</span></li>
      <li class="entry"><span class="part-name">Nome Peça</span><span class="part-leader"></span><span class="displacement">Cilindrada</span><span class="displacement-leader"></span><span class="page-number">005</span></li>
    </ul>
  </section>

  <section class="index-section section-2">
    <div class="tab-row">
      <div class="tab tab-maker">Nome Montadora</div><div class="tab-rule rule-maker"></div>
      <div class="tab tab-displacement">Cilindarada</div><div class="tab-rule rule-displacement"></div>
    </div>
    <ul class="entries">
      <li class="entry"><span class="part-name">Nome Peça</span><span class="part-leader"></span><span class="displacement">Cilindrada</span><span class="displacement-leader"></span><span class="page-number">006</span></li>
      <li class="entry"><span class="part-name">Nome Peça</span><span class="part-leader"></span><span class="displacement">Cilindrada</span><span class="displacement-leader"></span><span class="page-number">007</span></li>
      <li class="entry"><span class="part-name">Nome Peça</span><span class="part-leader"></span><span class="displacement">Cilindrada</span><span class="displacement-leader"></span><span class="page-number">008</span></li>
      <li class="entry"><span class="part-name">Nome Peça</span><span class="part-leader"></span><span class="displacement">Cilindrada</span><span class="displacement-leader"></span><span class="page-number">009</span></li>
      <li class="entry"><span class="part-name">Nome Peça</span><span class="part-leader"></span><span class="displacement">Cilindrada</span><span class="displacement-leader"></span><span class="page-number">010</span></li>
    </ul>
  </section>

  <section class="index-section section-3">
    <div class="tab-row">
      <div class="tab tab-maker">Nome Montadora</div><div class="tab-rule rule-maker"></div>
      <div class="tab tab-displacement">Cilindarada</div><div class="tab-rule rule-displacement"></div>
    </div>
    <ul class="entries">
      <li class="entry"><span class="part-name">Nome Peça</span><span class="part-leader"></span><span class="displacement">Cilindrada</span><span class="displacement-leader"></span><span class="page-number">011</span></li>
      <li class="entry"><span class="part-name">Nome Peça</span><span class="part-leader"></span><span class="displacement">Cilindrada</span><span class="displacement-leader"></span><span class="page-number">012</span></li>
      <li class="entry"><span class="part-name">Nome Peça</span><span class="part-leader"></span><span class="displacement">Cilindrada</span><span class="displacement-leader"></span><span class="page-number">013</span></li>
      <li class="entry"><span class="part-name">Nome Peça</span><span class="part-leader"></span><span class="displacement">Cilindrada</span><span class="displacement-leader"></span><span class="page-number">014</span></li>
      <li class="entry"><span class="part-name">Nome Peça</span><span class="part-leader"></span><span class="displacement">Cilindrada</span><span class="displacement-leader"></span><span class="page-number">015</span></li>
    </ul>
  </section>
</main>
</body>
</html>
```